A start-up named "brivora" - a clinical research organization needs a new PowerPoint design

We need a new PowerPoint Design (incl. business card and stationery design) for an early-stage start-up named "brivora" seeking to build an ecosystem/ strategic partner alliances or consortium of committed and active collaborators to guide important components of the clinical trial.

Our ultimate goal is to avoid false neutrals – therapies that have not been and may never be evaluated in clinical trials due to the costs and/ or complexity.

The final design should highlight our patient-centric approach, innovative study design supported with the novel AI platform to make a stronger impact on patient lives.

Please see the attached brief for more details.
Updates

Requesting the proposals on color-coding, business-card designs, clinical research visuals, and icons as well as stationery design.

Target Market(s)

Pharma/ Biotech Executives
Medical Institutions
Clinical Trial Participants (Patients)

Colors
e34398

Requirements
Must have
• Use the Color Version of purple/ magenta logo

```html
<!DOCTYPE html>
<html lang="en">
<head>
<meta charset="utf-8">
<title>brivora – brand presentation, palette and stationery</title>
<link href="https://fonts.googleapis.com/css2?family=Roboto:wght@400;500;700;900&family=Open+Sans:wght@400;600;700&display=swap" rel="stylesheet">
<style>
  :root{
    --magenta:#d7157b;
    --magenta-deep:#a0105c;
    --magenta-soft:#e04296;
    --purple:#6a2c91;
    --violet:#8e2aa6;
    --ink:#1c0f18;
    --text:#333333;
    --muted:#8c8c8c;
    --panel:#dedee0;
    --panel-light:#ececee;
    --white:#ffffff;
    --lilac:#e9c3f0;
    --lilac-line:#c86bd8;
  }
  *{box-sizing:border-box;margin:0;padding:0}
  html,body{width:1005px;height:1200px;overflow:hidden;background:var(--white)}
  body{font-family:"Roboto",Arial,sans-serif;color:var(--text)}
  .canvas{position:relative;width:1005px;height:1200px;overflow:hidden}
  .abs{position:absolute}

  /* left column */
  .band{position:absolute;left:0;width:480px;background:linear-gradient(118deg,var(--panel-light) 0 46%,var(--panel) 46% 100%);border-bottom:2px solid #f4f4f5}
  .slide{position:absolute;left:53px;width:367px;height:207px;background:var(--white);overflow:hidden;box-shadow:3px 4px 6px rgba(0,0,0,.35)}
  .slide--dark{background:linear-gradient(160deg,#241420 0%,var(--ink) 55%,#120a10 100%)}
  .network-art{position:absolute;left:0;top:0;width:367px;height:180px;background:radial-gradient(circle at 30% 35%,rgba(90,60,80,.35),transparent 45%),radial-gradient(circle at 82% 75%,rgba(120,40,80,.25),transparent 35%)}
  .wave{position:absolute;left:0;bottom:0;width:100%}
  .slide-title{position:absolute;left:0;width:100%;text-align:center;font-weight:700}
  .slide-rule{position:absolute;height:0;border-top:1.2px solid #555}
  .footer-mark{position:absolute;right:10px;bottom:7px;font:700 9px "Roboto",sans-serif;color:var(--magenta)}
  .wordmark{font-family:"Roboto",Arial,sans-serif;font-weight:700;color:var(--magenta);letter-spacing:-.5px;white-space:nowrap;display:inline-flex;align-items:flex-start}
  .wordmark .dot{display:inline-block;background:currentColor;margin-left:.08em}

  .reason-card{position:absolute;top:86px;height:104px;border:1px solid #a9a9a9;border-radius:6px;background:#f7f7f7}
  .reason-label{position:absolute;top:113px;width:110px;text-align:center;font:700 7.5px "Roboto",sans-serif;color:#333}
  .reason-note{position:absolute;top:143px;width:110px;text-align:center;font:400 5.6px/1.3 "Roboto",sans-serif;color:#555}
  .ring{position:absolute;top:63px;width:46px;height:46px}

  .stat-box{position:absolute;background:var(--lilac);border:1px solid var(--lilac-line);font:400 6.8px/1.35 "Roboto",sans-serif;color:#333;display:flex;align-items:center;justify-content:center;text-align:center;padding:6px 10px}

  /* palette */
  .palette{position:absolute;left:480px;top:0;width:525px;height:301px;background:var(--white)}
  .section-title{position:absolute;font:400 20px "Open Sans",sans-serif;letter-spacing:1px;color:#9a9a9a}
  .swatch-row{position:absolute;left:44px;display:flex;height:22px;width:186px}
  .swatch-row span{flex:1}
  .swatch-name{position:absolute;left:239px;font:400 9px "Open Sans",sans-serif;color:#8a8a8a;letter-spacing:.3px}

  /* right panels */
  .panel{position:absolute;left:480px;width:525px;background:linear-gradient(135deg,var(--panel-light) 0 52%,var(--panel) 52% 100%)}
  .panel--card{top:301px;height:338px;border:1px solid #9a9a9a}
  .panel--letter{top:640px;height:560px}
  .panel .section-title{left:26px;color:var(--muted)}

  .biz-card{position:absolute;left:41px;top:48px;width:444px;height:256px;background:var(--white);overflow:hidden;box-shadow:2px 3px 6px rgba(0,0,0,.3);font-family:"Open Sans",sans-serif}
  .biz-name{position:absolute;right:21px;top:86px;text-align:right;color:#222}
  .biz-name strong{display:block;font:700 17px "Open Sans",sans-serif;letter-spacing:.3px}
  .biz-name span{display:block;font:400 14px "Open Sans",sans-serif;margin-top:0;padding-right:21px}
  .biz-rule{position:absolute;left:5px;right:5px;top:135px;border-top:1.5px solid var(--magenta)}
  .contact{position:absolute;font:400 9.6px/1.25 "Open Sans",sans-serif;color:#222;white-space:nowrap}
  .icon{position:absolute;color:#333}
  .biz-url{position:absolute;right:45px;bottom:4px;font:700 10px "Open Sans",sans-serif;color:var(--white)}

  .letter{position:absolute;left:83px;top:51px;width:337px;height:474px;background:var(--white);overflow:hidden;box-shadow:2px 3px 6px rgba(0,0,0,.3);font-family:"Open Sans",sans-serif}
  .letter-texture{position:absolute;left:120px;top:0;width:217px;height:110px;background:linear-gradient(200deg,#ececec 0%,rgba(255,255,255,0) 70%)}
  .letter-rule{position:absolute;left:15px;width:315px;top:73px;border-top:1px solid #c8c8c8}
  .sender{position:absolute;left:43px;top:99px;font:400 5.3px/7.6px "Open Sans",sans-serif;color:#222}
  .sender b{font-weight:600}
  .letter-date{position:absolute;right:53px;top:129px;font:600 5.3px "Open Sans",sans-serif;color:#222}
  .letter-body p{position:absolute;left:43px;width:253px;font:400 5.2px/10.9px "Open Sans",sans-serif;color:#333}
  .signature-art{position:absolute;left:43px;top:335px;width:56px;height:14px;background:linear-gradient(90deg,#e6e6e6,#f5f5f5)}
  .signer{position:absolute;left:43px;top:352px;font:700 5.4px "Open Sans",sans-serif;color:#222}
  .signer-role{position:absolute;left:43px;top:360px;font:400 3.6px "Open Sans",sans-serif;color:#888}
  .letter-contact{position:absolute;left:46px;font:400 5px "Open Sans",sans-serif;color:#444;white-space:nowrap}
  .letter-icon{position:absolute;left:35px;width:7px;height:7px;color:#444}
</style>
</head>
<body>
<svg width="0" height="0" style="position:absolute" aria-hidden="true">
  <defs>
    <linearGradient id="magentaBand" x1="0" x2="1" y1="0" y2="0">
      <stop offset="0" stop-color="#a0105c"/><stop offset=".55" stop-color="#c8176f"/><stop offset="1" stop-color="#e3177f"/>
    </linearGradient>
    <linearGradient id="ringGrad" x1="0" x2="1" y1="0" y2="1">
      <stop offset="0" stop-color="#8e2aa6"/><stop offset="1" stop-color="#e3177f"/>
    </linearGradient>
    <symbol id="wave" viewBox="0 0 400 60" preserveAspectRatio="none">
      <path d="M0 16 C 90 40 190 46 300 32 C 345 26 375 18 400 8 L400 18 C 330 34 230 50 150 51 C 90 51 40 40 0 27 Z" fill="currentColor"/>
      <path d="M0 38 C 100 62 220 56 400 22 L400 60 L0 60 Z" fill="url(#magentaBand)"/>
    </symbol>
    <symbol id="ico-mail" viewBox="0 0 24 24"><rect x="2.5" y="5" width="19" height="14" rx="2" fill="none" stroke="currentColor" stroke-width="1.6"/><polyline points="3,6 12,13 21,6" fill="none" stroke="currentColor" stroke-width="1.6"/></symbol>
    <symbol id="ico-globe" viewBox="0 0 24 24"><circle cx="12" cy="12" r="10" fill="none" stroke="currentColor" stroke-width="1.6"/><ellipse cx="12" cy="12" rx="4.5" ry="10" fill="none" stroke="currentColor" stroke-width="1.4"/><path d="M2 12h20M4 7h16M4 17h16" stroke="currentColor" stroke-width="1.3"/></symbol>
    <symbol id="ico-pin" viewBox="0 0 24 24"><path d="M12 22.5s-7.5-7.3-7.5-12.5a7.5 7.5 0 0 1 15 0c0 5.2-7.5 12.5-7.5 12.5z" fill="none" stroke="currentColor" stroke-width="1.6"/><circle cx="12" cy="10" r="2.8" fill="none" stroke="currentColor" stroke-width="1.5"/></symbol>
    <symbol id="ico-phone" viewBox="0 0 24 24"><circle cx="12" cy="12" r="10.2" fill="none" stroke="currentColor" stroke-width="1.6"/><path d="M8.5 7.2c.5-.5 1.3-.5 1.8 0l1 1.2c.4.5.3 1.1-.1 1.5l-.6.5c.6 1.2 1.6 2.2 2.8 2.8l.5-.6c.4-.4 1-.5 1.5-.1l1.2 1c.5.5.5 1.3 0 1.8l-.7.7c-.8.8-2.4.8-4-.3-1.6-1-3-2.4-4-4-1.1-1.6-1.1-3.2-.3-4z" fill="currentColor"/></symbol>
    <symbol id="ico-fax" viewBox="0 0 24 24"><rect x="6" y="2.5" width="12" height="6" fill="none" stroke="currentColor" stroke-width="1.6"/><rect x="2.5" y="8.5" width="19" height="9" rx="1.5" fill="none" stroke="currentColor" stroke-width="1.6"/><rect x="6" y="14" width="12" height="7.5" fill="#fff" stroke="currentColor" stroke-width="1.6"/><path d="M8 17h8M8 19.5h6" stroke="currentColor" stroke-width="1.2"/></symbol>
  </defs>
</svg>

<main class="canvas">

  <!-- Presentation column -->
  <div class="band" style="top:0;height:264px"></div>
  <div class="band" style="top:264px;height:225px"></div>
  <div class="band" style="top:489px;height:223px"></div>
  <div class="band" style="top:712px;height:225px"></div>
  <div class="band" style="top:937px;height:263px;border-bottom:none"></div>

  <!-- Title slide -->
  <section class="slide slide--dark" style="top:47px" aria-label="Title slide">
    <div class="network-art" role="img" aria-label="Faint molecular network decoration"></div>
    <div class="abs" style="left:82px;top:76px;font-size:44px">
      <span class="wordmark">brivora<span class="dot" style="width:9px;height:9px;margin-top:8px"></span></span>
    </div>
    <svg class="wave" width="367" height="45" style="color:#6d6d6d"><use href="#wave" width="367" height="45"/></svg>
  </section>

  <!-- Drug development slide -->
  <section class="slide" style="top:272px" aria-label="New drug development process">
    <h2 class="slide-title" style="top:10px;font-size:12.5px;color:var(--purple);letter-spacing:.3px">NEW DRUG DEVELOPMENT PROCESS</h2>
    <div class="slide-rule" style="left:64px;width:240px;top:30px"></div>

    <svg class="abs" style="left:0;top:0" width="367" height="207" font-family="Roboto, sans-serif">
      <g transform="translate(108 120)">
        <circle r="64" fill="none" stroke="#c2177a" stroke-width="3"/>
        <path d="M0 0 L0 -60 A60 60 0 0 1 59.1 10.4 Z" fill="#a0105c"/>
        <path d="M0 0 L57.1 10.1 A58 58 0 0 1 15 56 Z" fill="#c8176f"/>
        <path d="M0 0 L15 56 A58 58 0 0 1 -47.5 33.3 Z" fill="#e0569a"/>
        <path d="M0 0 L-47.5 33.3 A58 58 0 0 1 -54.5 -19.8 Z" fill="#e87cb3"/>
        <path d="M0 0 L-54.5 -19.8 A58 58 0 0 1 0 -58 Z" fill="#f0a8cf"/>
        <path d="M-5 -70 L8 -61 L-3 -54 Z" fill="#c2177a"/>
        <circle r="5.5" fill="#fff"/>
        <g fill="#fff" font-size="3.6" font-weight="700" text-anchor="middle">
          <text x="27" y="-38">DRUG DISCOVER</text><text x="27" y="-34">&amp; LAB RESEARCH</text>
          <text x="27" y="-27" font-weight="400">5000-10,000</text><text x="27" y="-23" font-weight="400">potential drugs</text>
          <text x="36" y="6">PRECLINICAL</text><text x="36" y="10">TESTING</text>
          <text x="36" y="16" font-weight="400">250-300</text><text x="36" y="20" font-weight="400">Potential drugs</text>
          <text x="0" y="30">CLINICAL TRIALS</text>
          <text x="0" y="36" font-weight="400">phase I, II, III</text><text x="0" y="40" font-weight="400">1,120-5600</text><text x="0" y="44" font-weight="400">Human test subjects</text>
          <text x="-32" y="3">PRECOMMERCIALIZATION</text>
          <text x="-32" y="11" font-weight="400">1 st approved drug</text>
          <text x="-26" y="-18" fill="#c2177a">COMMERCIALIZATION</text>
        </g>
      </g>
      <g fill="#666" font-size="3.4" text-anchor="middle">
        <text x="26" y="93">FDA</text><text x="26" y="97">approval</text>
        <path d="M36 93 L44 90 L40 97 Z" fill="#555"/>
        <text x="54" y="185">New Drug</text><text x="54" y="189">Application</text>
        <path d="M62 178 L68 173 L68 181 Z" fill="#555"/>
        <text x="160" y="183">New Drug</text><text x="160" y="187">Application</text>
        <path d="M150 176 L144 171 L145 179 Z" fill="#555"/>
      </g>

      <text x="276" y="68" text-anchor="middle" font-size="17" font-weight="700" fill="#555">85%</text>
      <text x="276" y="76" text-anchor="middle" font-size="6" font-weight="500" fill="#444">of clinical trials fail to</text>
      <text x="276" y="84" text-anchor="middle" font-size="6" font-weight="500" fill="#444">retain enough patients</text>
      <line x1="226" y1="88.5" x2="330" y2="88.5" stroke="#999" stroke-width=".6"/>

      <rect x="240" y="89" width="21" height="38" fill="#d9481c"/>
      <polygon points="240,126 261,126 248,143 248,179 204,179 204,147" fill="#f26522"/>
      <rect x="265" y="89" width="21" height="38" fill="#a0105c"/>
      <polygon points="265,126 286,126 297,141 297,179 255,179 255,141" fill="#c2177a"/>
      <rect x="290" y="89" width="21" height="38" fill="#4b2a96"/>
      <polygon points="290,126 311,126 348,146 348,179 304,179 304,150" fill="#5b3bb0"/>

      <g fill="#fff" text-anchor="middle">
        <text x="226" y="156" font-size="7.5" font-weight="700">70%</text>
        <text x="226" y="162" font-size="2.6">of potential participants</text>
        <text x="226" y="165" font-size="2.6">live far from the</text>
        <text x="226" y="168" font-size="2.6">nearest site</text>
        <text x="276" y="158" font-size="7.5" font-weight="700">67%</text>
        <text x="276" y="164" font-size="2.6">of sites fail to meet</text>
        <text x="276" y="167" font-size="2.6">enrolment goals</text>
        <text x="326" y="161" font-size="7.5" font-weight="700">30%</text>
        <text x="326" y="167" font-size="2.6">average drop out</text>
        <text x="326" y="170" font-size="2.6">rate</text>
      </g>
    </svg>
    <span class="footer-mark">brivora</span>
  </section>

  <!-- Enrolment slide -->
  <section class="slide" style="top:497px" aria-label="Why patients do not enrol">
    <h2 class="slide-title" style="top:9px;font-size:14.5px;color:#c2177a">Why don’t patients enrol in trials?</h2>
    <div class="slide-rule" style="left:64px;width:236px;top:30px"></div>
    <p class="slide-title" style="top:43px;font-size:9px;font-weight:500;color:#444">Reasons For Not Enrolling In A Clinical Trial</p>

    <div class="reason-card" style="left:37px;width:77px"></div>
    <div class="reason-card" style="left:140px;width:82px"></div>
    <div class="reason-card" style="left:246px;width:77px"></div>

    <svg class="ring" style="left:51px" viewBox="0 0 46 46"><circle cx="23" cy="23" r="21" fill="#fff"/><circle cx="23" cy="23" r="18" fill="none" stroke="#d0d0d0" stroke-width="4"/><circle cx="23" cy="23" r="18" fill="none" stroke="url(#ringGrad)" stroke-width="4" stroke-dasharray="75.8 113.1" transform="rotate(-90 23 23)"/><text x="23" y="27" text-anchor="middle" font-family="Roboto,sans-serif" font-weight="700" font-size="11.5" fill="#c2177a">67<tspan font-size="8">%</tspan></text></svg>
    <svg class="ring" style="left:158px" viewBox="0 0 46 46"><circle cx="23" cy="23" r="21" fill="#fff"/><circle cx="23" cy="23" r="18" fill="none" stroke="#d0d0d0" stroke-width="4"/><circle cx="23" cy="23" r="18" fill="none" stroke="url(#ringGrad)" stroke-width="4" stroke-dasharray="74.6 113.1" transform="rotate(-90 23 23)"/><text x="23" y="27" text-anchor="middle" font-family="Roboto,sans-serif" font-weight="700" font-size="11.5" fill="#c2177a">66<tspan font-size="8">%</tspan></text></svg>
    <svg class="ring" style="left:262px" viewBox="0 0 46 46"><circle cx="23" cy="23" r="21" fill="#fff"/><circle cx="23" cy="23" r="18" fill="none" stroke="#d0d0d0" stroke-width="4"/><circle cx="23" cy="23" r="18" fill="none" stroke="url(#ringGrad)" stroke-width="4" stroke-dasharray="63.3 113.1" transform="rotate(-90 23 23)"/><text x="23" y="27" text-anchor="middle" font-family="Roboto,sans-serif" font-weight="700" font-size="11.5" fill="#c2177a">56<tspan font-size="8">%</tspan></text></svg>

    <p class="reason-label" style="left:20px">TRUST</p>
    <p class="reason-label" style="left:126px">UNDERSTANDING</p>
    <p class="reason-label" style="left:230px">CONVENIENCE</p>
    <p class="reason-note" style="left:21px">INSUFFICIENT<br>STAFF TIME</p>
    <p class="reason-note" style="left:126px">LENGTH AND COMPLEXITY<br>OF CONSENT FORM</p>
    <p class="reason-note" style="left:230px">TRANSPORTATION<br>TO TRIAL VISITS</p>
    <span class="footer-mark">brivora</span>
  </section>

  <!-- AI slide -->
  <section class="slide" style="top:722px" aria-label="AI in clinical trial analysis">
    <h2 class="slide-title" style="top:9px;font-size:14.5px;color:#c2177a">AI as a solution in clinical trial analysis</h2>
    <div class="slide-rule" style="left:49px;width:269px;top:33px"></div>
    <p class="abs" style="left:24px;top:46px;font:700 6.8px Roboto,sans-serif;color:#333">Top three digital challenges sponsors identified</p>
    <ol class="abs" style="left:32px;top:62px;font:400 6.6px/8.3px Roboto,sans-serif;color:#444;padding-left:0;list-style:none">
      <li>1. Digital technology and AI to improve</li>
      <li style="padding-left:8px">clinical traffic efficiency</li>
      <li>2. Analyze complex data sets</li>
      <li>3. Integrate data from disparate source</li>
    </ol>
    <div class="abs" role="img" aria-label="Illustration of a brain drawn as a circuit board" style="left:31px;top:104px;width:119px;height:85px;background:radial-gradient(circle at 50% 50%,#6a6a6a 0%,#2e2e2e 55%,#1a1a1a 100%)"></div>
    <div class="stat-box" style="left:225px;top:50px;width:115px;height:60px;text-align:left;justify-content:flex-start">80% of the 350 respondents in biopharma report that they plan touse AI or big data analytics within 5 years</div>
    <div class="stat-box" style="left:226px;top:122px;width:115px;height:60px">55% of respondents said they were partnering with tech companies to help expand data gathering/ processing capacity.</div>
  </section>

  <!-- Closing slide -->
  <section class="slide slide--dark" style="top:952px" aria-label="Closing slide">
    <div class="network-art" role="img" aria-label="Faint molecular network decoration"></div>
    <p class="abs" style="left:80px;top:68px;font:700 37px Roboto,sans-serif;color:#fff;letter-spacing:.5px">Thank You</p>
    <div class="abs" style="left:139px;top:136px;font-size:19px">
      <span class="wordmark" style="color:#fff">brivora<span class="dot" style="width:4px;height:4px;margin-top:3px"></span></span>
    </div>
    <svg class="wave" width="367" height="45" style="color:#6d6d6d"><use href="#wave" width="367" height="45"/></svg>
  </section>

  <!-- Colour palette -->
  <section class="palette" aria-label="Colour palette">
    <h2 class="section-title" style="left:61px;top:22px">COLOR PATTETE</h2>
    <p class="abs" style="left:347px;top:33px;font:400 8.8px 'Open Sans',sans-serif;color:#666">SOME GRADIENT COMBINATION</p>

    <div class="swatch-row" style="top:83px"><span style="background:#006b35"></span><span style="background:#009245"></span><span style="background:#39a96b"></span><span style="background:#63bf8a"></span><span style="background:#97d4b0"></span></div>
    <p class="swatch-name" style="top:87px">OPTION #1</p>
    <div class="swatch-row" style="top:113px"><span style="background:#6b6e2b"></span><span style="background:#8f963a"></span><span style="background:#a8ae63"></span><span style="background:#c0c28a"></span><span style="background:#d6d7b1"></span></div>
    <p class="swatch-name" style="top:119px">OPTION #2</p>
    <div class="swatch-row" style="top:147px"><span style="background:#a0105c"></span><span style="background:#d7157b"></span><span style="background:#e04296"></span><span style="background:#e872ae"></span><span style="background:#f0a3cb"></span></div>
    <p class="swatch-name" style="top:153px;left:237px">LOGO COLOR GRADE</p>
    <div class="swatch-row" style="top:183px"><span style="background:#6b1f6e"></span><span style="background:#93278f"></span><span style="background:#a653a9"></span><span style="background:#bb7fc0"></span><span style="background:#d3a9d6"></span></div>
    <p class="swatch-name" style="top:189px;left:242px">OPTION #3</p>
    <div class="swatch-row" style="top:214px"><span style="background:#b07040"></span><span style="background:#e8915a"></span><span style="background:#eda77a"></span><span style="background:#f2c3a0"></span><span style="background:#f7d8c2"></span></div>
    <p class="swatch-name" style="top:218px;left:242px">OPTION #4</p>
    <div class="swatch-row" style="top:244px"><span style="background:#4d4d4d"></span><span style="background:#666666"></span><span style="background:#808080"></span><span style="background:#999999"></span><span style="background:#b3b3b3"></span></div>
    <p class="swatch-name" style="top:249px;left:240px">OPTION #5</p>

    <svg class="abs" style="left:0;top:0" width="525" height="301" font-family="Roboto, sans-serif">
      <defs>
        <linearGradient id="dBlue" x1="0" y1="0" x2="1" y2="1"><stop offset="0" stop-color="#2f7fd6"/><stop offset="1" stop-color="#0d3f8f"/></linearGradient>
        <linearGradient id="dMag" x1="0" y1="0" x2="1" y2="1"><stop offset="0" stop-color="#e83f96"/><stop offset="1" stop-color="#8c0f52"/></linearGradient>
        <linearGradient id="dOrange" x1="0" y1="0" x2="1" y2="1"><stop offset="0" stop-color="#ffa11a"/><stop offset="1" stop-color="#e0451d"/></linearGradient>
        <linearGradient id="dPurple" x1="0" y1="0" x2="1" y2="1"><stop offset="0" stop-color="#7a4fc0"/><stop offset="1" stop-color="#3b2380"/></linearGradient>
        <linearGradient id="dGreen" x1="0" y1="0" x2="1" y2="1"><stop offset="0" stop-color="#4fe08a"/><stop offset="1" stop-color="#0f9a3e"/></linearGradient>
      </defs>
      <g stroke-width="1.2">
        <line x1="365" y1="94" x2="400" y2="94" stroke="#1f5fb5"/><circle cx="365" cy="94" r="2" fill="#1f5fb5"/>
        <line x1="455" y1="123" x2="493" y2="123" stroke="#c2177a"/><circle cx="493" cy="123" r="2" fill="#c2177a"/>
        <line x1="365" y1="153" x2="400" y2="153" stroke="#e85a1d"/><circle cx="365" cy="153" r="2" fill="#e85a1d"/>
        <line x1="455" y1="182" x2="493" y2="182" stroke="#5b3bb0"/><circle cx="493" cy="182" r="2" fill="#5b3bb0"/>
        <line x1="365" y1="211" x2="400" y2="211" stroke="#1fb455"/><circle cx="365" cy="211" r="2" fill="#1fb455"/>
      </g>
      <g fill="none" stroke="#fff" stroke-width=".6" stroke-dasharray="1.5 1.2">
        <polygon points="442,96 469,123 442,150 415,123" fill="url(#dMag)" stroke="none"/>
        <polygon points="442,100 465,123 442,146 419,123"/>
        <polygon points="442,155 469,182 442,209 415,182" fill="url(#dPurple)" stroke="none"/>
        <polygon points="442,159 465,182 442,205 419,182"/>
        <polygon points="413,67 440,94 413,121 386,94" fill="url(#dBlue)" stroke="none"/>
        <polygon points="413,71 436,94 413,117 390,94"/>
        <polygon points="413,126 440,153 413,180 386,153" fill="url(#dOrange)" stroke="none"/>
        <polygon points="413,130 436,153 413,176 390,153"/>
        <polygon points="413,184 440,211 413,238 386,211" fill="url(#dGreen)" stroke="none"/>
        <polygon points="413,188 436,211 413,234 390,211"/>
      </g>
      <g fill="#fff" text-anchor="middle" font-weight="700">
        <text x="413" y="89" font-size="2.6">OPTION</text><text x="413" y="100" font-size="11">01</text>
        <text x="442" y="118" font-size="2.6">OPTION</text><text x="442" y="129" font-size="11">02</text>
        <text x="413" y="148" font-size="2.6">OPTION</text><text x="413" y="159" font-size="11">03</text>
        <text x="442" y="177" font-size="2.6">OPTION</text><text x="442" y="188" font-size="11">04</text>
        <text x="413" y="206" font-size="2.6">OPTION</text><text x="413" y="217" font-size="11">05</text>
      </g>
    </svg>
  </section>

  <!-- Business card -->
  <section class="panel panel--card" aria-label="Business card">
    <h2 class="section-title" style="top:10px">BUSINESS CARD</h2>
    <article class="biz-card">
      <div class="abs" style="left:19px;top:22px;font-size:42px">
        <span class="wordmark">brivora<span class="dot" style="width:9px;height:9px;margin-top:7px"></span></span>
      </div>
      <div class="biz-name"><strong>Name Surname, PhD</strong><span>Managing partner</span></div>
      <div class="biz-rule"></div>

      <svg class="icon" style="left:28px;top:148px" width="14" height="14"><use href="#ico-mail"/></svg>
      <svg class="icon" style="left:28px;top:166px" width="14" height="14"><use href="#ico-globe"/></svg>
      <svg class="icon" style="left:28px;top:184px" width="16" height="18"><use href="#ico-pin"/></svg>
      <p class="contact" style="left:51px;top:147px">name.surname@brivora.ch</p>
      <p class="contact" style="left:52px;top:164px">www.brivora.ch</p>
      <p class="contact" style="left:52px;top:182px;line-height:12px">brivora GmbH<br>Street name 1<br>9999 City name<br>Switzerland</p>

      <svg class="icon" style="left:262px;top:151px" width="14" height="14"><use href="#ico-phone"/></svg>
      <svg class="icon" style="left:262px;top:170px" width="14" height="14"><use href="#ico-phone"/></svg>
      <svg class="icon" style="left:262px;top:188px" width="14" height="14"><use href="#ico-phone"/></svg>
      <svg class="icon" style="left:262px;top:206px" width="14" height="14"><use href="#ico-fax"/></svg>
      <p class="contact" style="left:281px;top:151px">Office:&nbsp;&nbsp; +41 (0)00 555 10 00</p>
      <p class="contact" style="left:281px;top:170px">Phone:&nbsp; +41 (0)00 555 10 20</p>
      <p class="contact" style="left:281px;top:188px">Mobile:&nbsp; +41 (0)70 555 43 21</p>
      <p class="contact" style="left:281px;top:206px">Fax:&nbsp;&nbsp; +41 (0)00 555 10 01</p>

      <svg class="wave" width="444" height="30" style="color:#3a3a3a"><use href="#wave" width="444" height="30"/></svg>
      <p class="biz-url">www.brivora.ch</p>
    </article>
  </section>

  <!-- Letterhead -->
  <section class="panel panel--letter" aria-label="Letterhead">
    <h2 class="section-title" style="top:11px">LETTERHEAD</h2>
    <article class="letter">
      <div class="letter-texture" role="img" aria-label="Soft diamond pattern decoration"></div>
      <div class="abs" style="left:25px;top:33px;font-size:19px">
        <span class="wordmark">brivora<span class="dot" style="width:4px;height:4px;margin-top:3px"></span></span>
      </div>
      <div class="letter-rule"></div>

      <div class="sender">
        <b>Lena Hart</b><br>Chief Director<br>
        <b>A</b> : 12 Orchard Lane, Singapore - 4410<br>
        <b>W</b> : mail@example-mail.com, www.sample-site.com<br>
        <b>P</b> : +65 - 55501 - 2468
      </div>
      <p class="letter-date">Date, 3 January, 2021</p>

      <div class="letter-body">
        <p style="top:158px">This is a sample letter that has been placed to demonstrate typing remat (Your Company). letterhead design. When positioned properly, it will serve to work in harmony with all other elements letterhead. This letterhead design is meant to project an image</p>
        <p style="top:201px">This letterhead design is meant project an image of professionalism reliability. By using simple aligen we have created a very spacious feeling. The simplicity suggest rengththe spaciousnes contributes h aesthetics the layout. These basic qualities along with the (Your Company)</p>
        <p style="top:245px">look and helps reinforce the (Your Company) brand. letterhead design is meant to project an image p design. When positioned properly, it will serve to work in harmony all the other elements letterhead. sionalism and reliability.</p>
        <p style="top:288px">This letterhead design is based on the (Form of your logo) form (Your Company) logo. Each stationery we have created a very spacious feeling. The simplicity suggests strength the spaciousnes contribute part of the (Form of your logo).</p>
      </div>

      <div class="signature-art" role="img" aria-label="Handwritten signature"></div>
      <p class="signer">Marc Ellison</p>
      <p class="signer-role">Managing partner</p>

      <svg class="letter-icon" style="top:398px"><use href="#ico-phone" width="7" height="7"/></svg>
      <svg class="letter-icon" style="top:409px"><use href="#ico-phone" width="7" height="7"/></svg>
      <svg class="letter-icon" style="top:419px"><use href="#ico-phone" width="7" height="7"/></svg>
      <svg class="letter-icon" style="top:430px"><use href="#ico-fax" width="7" height="7"/></svg>
      <p class="letter-contact" style="top:397px">Office:&nbsp;&nbsp; +41 (0)00 555 10 00</p>
      <p class="letter-contact" style="top:408px">Phone:&nbsp; +41 (0)00 555 10 20</p>
      <p class="letter-contact" style="top:418px">Mobile:&nbsp; +41 (0)70 555 43 21</p>
      <p class="letter-contact" style="top:429px">Fax:&nbsp;&nbsp; +41 (0)00 555 10 01</p>

      <svg class="wave" width="337" height="30" style="color:#3a3a3a"><use href="#wave" width="337" height="30"/></svg>
    </article>
  </section>

</main>
</body>
</html>
```